A.I. Software PowerPoint Presentation

We need a PowerPoint presentation design for our artificial intelligence product qvPilot.

We've attached our current PowerPoint to use as a base. This presentation is used to introduce and describe what the product is, how it works, why you need it, what makes it better than other solutions, and how to implement it.

We would like the PowerPoint design to be more professional-looking as we present to executives and CIOs of banks, government, and other large corporations. We are a tech startup and would like the design to convey the feel of innovation and high-tech, but also trustworthy, reputable, and capable, for the more conservative audiences.

The PowerPoint should have minimal use of animation (animate only if necessary). It should be modern and clean and not too busy.

We appreciate design work on all of the following: slide backgrounds, title slide, fonts, pictures used in the slides, layout, charts, graphics, comparison versus, etc. If you have any ideas for the slide contents, please also provide any suggestions/recommendations.

I've also attached our qvPilot logo if that is needed, as well as our brochure.

We look forward to your submissions!

EDIT:
I would like to add that we are using PowerPoint 2010 on a PC (.pptx file), and that the slides should be in 16:9 mainly but also with 4:3 version (if possible cut off the sides and squish in the content a little, no need to make a new set of slides) as sometimes we cannot control whose projector we are presenting on. Thanks

Target Market(s)

Enterprise clients, multi-national corporations,
banks, airlines, telecommunications, government

Industry/Entity Type

Software

Font styles to use
Serif
Sans Serif

Colors

Designer to choose colors to be used in the design.

Requirements
Nice to have
• Professional, clean-look, modern design
Should not have
• Should not look cheesy (i.e. tons of stock photos, business cliche pictures)
• Should not look over-done/over-the-top
• Should not look outdated

```html
<!DOCTYPE html>
<html lang="en">
<head>
<meta charset="utf-8">
<title>qvPilot – Context slides</title>
<link rel="stylesheet" href="https://fonts.googleapis.com/css2?family=Lato:wght@400;700;900&display=swap">
<style>
  :root {
    --board: #e6dccb;
    --slide: #ffffff;
    --navy: #1d5fb3;
    --sky: #3fb0ec;
    --ink: #4a4a4a;
    --faint: #e4e6e8;
    --photo-a: #2b2f36;
    --photo-b: #d9c2ad;
  }
  * { box-sizing: border-box; margin: 0; padding: 0; }
  html, body { width: 1200px; height: 2639px; overflow: hidden; }
  body { background: var(--board); font-family: "Lato", Arial, sans-serif; position: relative; }

  .slide {
    position: absolute; left: 88px; width: 1024px; height: 577px;
    background: var(--slide); box-shadow: 0 4px 12px rgba(0,0,0,.25); overflow: hidden;
  }
  .slide--one { top: 65px; }
  .slide--two { top: 683px; }
  .slide--three { top: 1302px; }
  .slide--four { top: 1920px; }

  .title { position: absolute; top: 30px; font-weight: 900; font-size: 40px; color: var(--navy); letter-spacing: .5px; }
  .subtitle { position: absolute; top: 76px; font-size: 17px; color: var(--ink); }
  .centered { left: 0; right: 0; text-align: center; }
  .left-aligned { left: 54px; }

  .page-no { position: absolute; font-size: 14px; color: var(--navy); font-weight: 700; }

  .brand { position: absolute; left: 50px; bottom: 14px; display: flex; align-items: center; gap: 6px;
    font-size: 20px; color: var(--sky); font-weight: 400; }
  .brand-dot { width: 18px; height: 18px; border-radius: 50%; background: var(--sky); }

  /* slide one */
  .side-band { position: absolute; left: 0; top: 0; width: 110px; height: 577px; }
  .column { position: absolute; top: 185px; width: 229px; text-align: center; }
  .column h3 { font-size: 20px; font-weight: 700; line-height: 1.3; height: 125px; display: flex; align-items: flex-start; justify-content: center; }
  .column .card { height: 165px; border: 3px solid; border-radius: 20px; display: flex; align-items: center; justify-content: center; }
  .c1 { left: 121px; } .c2 { left: 397px; } .c3 { left: 673px; }
  .navy { color: var(--navy); border-color: var(--navy); }
  .sky { color: var(--sky); border-color: var(--sky); }

  .partners { display: flex; flex-direction: column; align-items: center; gap: 6px; font-weight: 700; color: var(--navy); font-size: 19px; }
  .partners .row { display: flex; gap: 18px; }

  .icon-fill { width: 90px; height: 90px; border-radius: 50%; }
  .icon-fill.sky-fill { background: var(--sky); }
  .icon-fill.navy-fill { background: var(--navy); }

  /* slide two */
  .top-band { position: absolute; top: 0; left: 0; right: 0; height: 16px; display: flex; gap: 6px; }
  .top-band span:first-child { width: 50px; background: var(--navy); }
  .top-band span:last-child { flex: 1; background: var(--sky); }
  .bottom-band { position: absolute; bottom: 0; left: 0; right: 0; height: 18px; display: flex; gap: 6px; }
  .bottom-band span:first-child { flex: 1; background: var(--sky); }
  .bottom-band span:last-child { width: 42px; background: var(--navy); }
  .tile { position: absolute; top: 174px; width: 229px; height: 303px; border: 3px solid; }
  .tile h3 { height: 128px; color: #fff; font-size: 20px; font-weight: 700; line-height: 1.3; text-align: center; padding: 12px 14px 0; }
  .tile .tile-body { height: 169px; display: flex; align-items: center; justify-content: center; }
  .tile.navy h3 { background: var(--navy); }
  .tile.sky h3 { background: var(--sky); }
  .t1 { left: 121px; } .t2 { left: 397px; } .t3 { left: 673px; }

  /* rows on slides three and four */
  .row-card { position: absolute; left: 90px; width: 558px; height: 106px; border: 3px solid; border-radius: 14px; display: flex; align-items: center; }
  .row-card .row-icon { width: 200px; display: flex; justify-content: center; }
  .row-card p { font-size: 17px; font-weight: 700; line-height: 1.35; }
  .r1 { top: 151px; } .r2 { top: 273px; } .r3 { top: 392px; }
  .row-icon .icon-fill { width: 48px; height: 48px; }
  .mini-partners { display: flex; flex-direction: column; align-items: center; font-weight: 700; color: var(--navy); font-size: 15px; line-height: 1.25; }

  .dots { position: absolute; top: 104px; left: 0; right: 0; display: flex; justify-content: center; gap: 6px; }
  .dots span { width: 10px; height: 10px; border-radius: 50%; background: var(--sky); }

  .portrait { position: absolute; left: 702px; top: 207px; width: 228px; height: 370px;
    background: linear-gradient(180deg, var(--photo-b) 0%, var(--photo-b) 30%, var(--photo-a) 42%, var(--photo-a) 100%);
    border-radius: 90px 90px 0 0; }

  .faint-mark { position: absolute; left: 730px; top: 220px; width: 330px; height: 330px; border-radius: 50%; background: var(--faint); }
</style>
</head>
<body>

<section class="slide slide--one">
  <svg class="side-band" viewBox="0 0 110 577" preserveAspectRatio="none" aria-hidden="true">
    <path d="M0 0 H96 Q40 290 62 577 H0 Z" fill="var(--navy)"/>
    <path d="M96 0 Q40 290 62 577 H70 Q48 290 104 0 Z" fill="var(--sky)"/>
  </svg>
  <h1 class="title centered">CONTEXT</h1>
  <p class="subtitle centered">We’ve spent the last *25 years building end-to-end automation solutions for leading companies</p>

  <div class="column c1 navy">
    <h3>A track record of<br>long term<br>relationships with<br>top companies</h3>
    <div class="card navy">
      <div class="partners"><div class="row"><span>Halvexa</span><span>Ostrapay</span></div><span>Drivorum</span></div>
    </div>
  </div>
  <div class="column c2 sky">
    <h3>Experts in custom<br>automation +<br>business intelligence<br>systems</h3>
    <div class="card sky"><div class="icon-fill sky-fill" role="img" aria-label="Icon of a head with circulating arrows"></div></div>
  </div>
  <div class="column c3 navy">
    <h3>Toronto – based,<br>but with a growing<br>global footprint</h3>
    <div class="card navy"><div class="icon-fill navy-fill" role="img" aria-label="Icon of a globe held in two hands"></div></div>
  </div>

  <div class="brand"><span class="brand-dot"></span>qvPilot</div>
  <span class="page-no" style="right:24px;bottom:16px">4</span>
</section>

<section class="slide slide--two">
  <div class="top-band"><span></span><span></span></div>
  <h1 class="title left-aligned" style="top:26px">CONTEXT</h1>
  <p class="subtitle left-aligned" style="top:78px">We’ve spent the last *25 years building end-to-end automation solutions for leading companies</p>
  <span class="page-no" style="right:24px;top:40px">3</span>

  <div class="tile t1 navy">
    <h3>A track record of<br>long term<br>relationships with<br>top companies</h3>
    <div class="tile-body"><div class="partners"><div class="row"><span>Halvexa</span><span>Ostrapay</span></div><span>Drivorum</span></div></div>
  </div>
  <div class="tile t2 sky">
    <h3>Experts in custom<br>automation +<br>business intelligence<br>systems</h3>
    <div class="tile-body"><div class="icon-fill sky-fill" role="img" aria-label="Icon of a head with circulating arrows"></div></div>
  </div>
  <div class="tile t3 navy">
    <h3>Toronto – based,<br>but with a growing<br>global footprint</h3>
    <div class="tile-body"><div class="icon-fill navy-fill" role="img" aria-label="Icon of a globe held in two hands"></div></div>
  </div>

  <div class="brand" style="bottom:22px;left:52px"><span class="brand-dot"></span>qvPilot</div>
  <div class="bottom-band"><span></span><span></span></div>
</section>

<section class="slide slide--three">
  <h1 class="title centered">CONTEXT</h1>
  <p class="subtitle centered">We’ve spent the last *25 years building end-to-end automation solutions for leading companies</p>
  <div class="dots"><span></span><span></span></div>

  <div class="row-card r1 navy">
    <div class="row-icon"><div class="mini-partners"><span>Halvexa · Ostrapay</span><span>Drivorum</span></div></div>
    <p>A track record of long term<br>relationships with top companies</p>
  </div>
  <div class="row-card r2 sky">
    <div class="row-icon"><div class="icon-fill sky-fill" role="img" aria-label="Icon of a head with circulating arrows"></div></div>
    <p>Experts in custom automation +<br>business intelligence systems</p>
  </div>
  <div class="row-card r3 navy">
    <div class="row-icon"><div class="icon-fill navy-fill" role="img" aria-label="Icon of a globe held in two hands"></div></div>
    <p>Toronto – based, but with a growing<br>global footprint</p>
  </div>

  <div class="portrait" role="img" aria-label="Photo of a smiling businessman in a dark suit with arms crossed"></div>

  <div class="brand"><span class="brand-dot"></span>qvPilot</div>
  <span class="page-no" style="right:24px;bottom:16px">5</span>
</section>

<section class="slide slide--four">
  <h1 class="title left-aligned">CONTEXT</h1>
  <p class="subtitle left-aligned">We’ve spent the last *25 years building end-to-end automation solutions for leading companies</p>

  <div class="faint-mark" aria-hidden="true"></div>

  <div class="row-card r1 navy">
    <div class="row-icon"><div class="mini-partners"><span>Halvexa · Ostrapay</span><span>Drivorum</span></div></div>
    <p>A track record of long term<br>relationships with top companies</p>
  </div>
  <div class="row-card r2 sky">
    <div class="row-icon"><div class="icon-fill sky-fill" role="img" aria-label="Icon of a head with circulating arrows"></div></div>
    <p>Experts in custom automation +<br>business intelligence systems</p>
  </div>
  <div class="row-card r3 navy">
    <div class="row-icon"><div class="icon-fill navy-fill" role="img" aria-label="Icon of a globe held in two hands"></div></div>
    <p>Toronto – based, but with a growing<br>global footprint</p>
  </div>

  <div class="brand"><span class="brand-dot"></span>qvPilot</div>
  <span class="page-no" style="right:24px;bottom:16px">6</span>
</section>

</body>
</html>
```